Billboard Design for Helicopter Tours (2 Designs) **URGENT PROJECT**

**URGENT PROJECT: We will award quickly to designers who submit fast, high quality work**

**PLEASE READ CAREFULLY SO WE NEED THE LEAST AMOUNT OF REVISIONS**

PROJECT OVERVIEW
We need a redesigned billboard banner using our exact red helicopter (from the Google Drive link below). Our current billboard is too crowded and the catch phrase, logo and URL is too small! The new versions must be clean, bold, premium, and helicopter focused. Also the catch phrase and website URL must be larger and more noticeable. You will create two (2) billboard designs.

DESIGN #1: Enlarged Red Helicopter + One Tone Background (No Photo Background)
• Use the exact red helicopter from our provided photos. You have to crop out the helicopter.
• Enlarge it significantly so it becomes the dominant focal point.
• Background must be one solid color (designer may propose the best tone).
• No background images.
• Helicopter must be crisp, clean, premium, with no fade or transparency.

DESIGN #2: Enlarged Red Helicopter + Beach Background Image
• Use the same red helicopter, enlarged and placed in front of the background.
• Background: Use the beach photo from our Google Drive.
• Left side of the background must be black faded so the text stands out clearly.
• The helicopter must remain fully bright, sharp, and NOT faded — it must sit in front of the background with strong visual separation.
• Overall feel: premium, exciting, tourism oriented.

TEXT REQUIREMENTS:
Catch Phrase:Gulfside Rotor Flights
Required Elements:
• skyNOMAD.com
• {Logo} Use our logo with the SN icon on the left side in all white

TYPOGRAPHY REQUIREMENTS
• Use the exact same font used in the word “Check” from our current billboard (see uploaded PDF).
• One font only across the entire design.
• Catch phrase font must be white.
• Text must be large, bold, and readable from a distance — our current design is too small.
• The website skyNOMAD.com must be enlarged and visually highlighted — current version is too small.

FILES PROVIDED
Google Drive:
https://files.example-share.net/folders/7qzRmTbw2LpXkA9dNcYhUe3GsVjo51K?view=link

BILLBOARD SPECIFICATIONS (IMPORTANT — MUST MATCH EXACTLY)
Digital Bulletin — 14' x 48'
• Display Resolution: 208 px (height) × 720 px (width)
• Mechanical Size: 208 px × 720 px
• File Formats: JPEG and PDF
• Color Mode: sRGB
• Bright white discouraged — if used, target R235 / G235 / B235
• Artwork must be delivered at exact 1:1 pixel ratio (no scaling, no DPI adjustments)

Target Market(s)

The target market includes tourists, couples, families, and locals seeking memorable, exciting, and visually striking experiences in Tampa and St. Pete.

Industry/Entity Type

Tourism, aerial sightseeing, adventure experiences, and local attractions.

Requirements
Must have
• The must haves are the exact red helicopter from our files, a clean premium layout, the correct SN‑left‑aligned logo, the catch phrase “Gulfside Rotor Flights,” the enlarged skyNOMAD.com URL, the correct font, and artwork delivered at the exact required billboard resolution.
Nice to have
• The nice to haves are subtle atmospheric enhancements, designer‑proposed background tones, and creative layout refinements that keep the helicopter dominant while enhancing the premium tourism feel.
Should not have
• The should not haves are any alternate helicopters, cluttered layouts, multiple fonts, or incorrect billboard dimensions.

```html
<!DOCTYPE html>
<html lang="en">
<head>
<meta charset="UTF-8">
<title>skyNOMAD.com — Gulfside Rotor Flights Billboard</title>
<link href="https://fonts.googleapis.com/css2?family=Montserrat:wght@600;800&display=swap" rel="stylesheet">
<style>
  :root {
    --page-bg: #eef1f4;
    --overlay-blue: #2f6fa3;
    --overlay-blue-soft: rgba(56, 128, 182, 0.6);
    --sand: #eadfbd;
    --sea: #a6dcc0;
    --sea-deep: #72c6b2;
    --heli-red: #d8262a;
    --heli-red-deep: #a8161b;
    --band-gold: #f0b12e;
    --band-orange: #f29a22;
    --band-edge: #f6d36a;
    --text-white: #ebebeb;
    --shadow-dark: rgba(20, 40, 70, 0.6);
  }
  * { margin: 0; padding: 0; box-sizing: border-box; }
  html, body {
    width: 1200px;
    height: 1045px;
    overflow: hidden;
    background: var(--page-bg);
    font-family: "Montserrat", sans-serif;
  }
  .billboard {
    position: absolute;
    left: 40px;
    top: 360px;
    width: 1120px;
    height: 325px;
    overflow: hidden;
  }
  .billboard__photo {
    position: absolute;
    inset: 0;
    background:
      linear-gradient(100deg, var(--overlay-blue) 0%, var(--overlay-blue-soft) 36%, rgba(120, 170, 200, 0.18) 52%, rgba(0,0,0,0) 64%),
      linear-gradient(160deg, var(--sand) 0%, #e2e4c8 40%, var(--sea) 70%, var(--sea-deep) 100%);
  }
  .billboard__helicopter {
    position: absolute;
    left: 590px;
    top: 40px;
    width: 530px;
    height: 220px;
    border-radius: 50% 40% 45% 50%;
    background: radial-gradient(ellipse at 40% 55%, var(--heli-red) 0%, var(--heli-red-deep) 45%, rgba(168, 22, 27, 0.55) 65%, rgba(168, 22, 27, 0) 78%);
  }
  .billboard__band {
    position: absolute;
    inset: 0;
    width: 100%;
    height: 100%;
  }
  .brand {
    position: absolute;
    left: 118px;
    top: 40px;
    display: flex;
    align-items: center;
    gap: 14px;
  }
  .brand__dot {
    width: 38px;
    height: 38px;
    border: 3px solid var(--text-white);
    border-radius: 50%;
  }
  .brand__name {
    font-weight: 600;
    font-size: 34px;
    color: var(--text-white);
    letter-spacing: 0.5px;
  }
  .headline {
    position: absolute;
    left: 8px;
    top: 116px;
    width: 560px;
    text-align: center;
    font-weight: 800;
    font-size: 54px;
    line-height: 0.9;
    color: var(--text-white);
    text-transform: uppercase;
    text-shadow: 2px 3px 0 var(--shadow-dark);
  }
  .site-link {
    position: absolute;
    left: 44px;
    top: 258px;
    display: flex;
    align-items: center;
    gap: 12px;
  }
  .site-link__icon { width: 30px; height: 30px; }
  .site-link__url {
    font-weight: 800;
    font-size: 36px;
    letter-spacing: 2px;
    color: var(--text-white);
    text-transform: uppercase;
    text-shadow: 2px 2px 0 rgba(150, 90, 10, 0.55);
  }
</style>
</head>
<body>
  <section class="billboard">
    <div class="billboard__photo" role="img" aria-label="Aerial photo of a sandy beach with rows of umbrellas and turquoise shallow water"></div>
    <div class="billboard__helicopter" role="img" aria-label="Large red tour helicopter flying over the beach, facing left"></div>

    <svg class="billboard__band" viewBox="0 0 1120 325" preserveAspectRatio="none" aria-hidden="true">
      <defs>
        <linearGradient id="bandFill" x1="0" y1="0" x2="1" y2="0">
          <stop offset="0" stop-color="var(--band-gold)"/>
          <stop offset="1" stop-color="var(--band-orange)"/>
        </linearGradient>
      </defs>
      <path d="M0 236 Q 240 210 680 325 L0 325 Z" fill="var(--band-edge)" opacity="0.45"/>
      <path d="M0 250 Q 250 220 650 325 L0 325 Z" fill="url(#bandFill)"/>
    </svg>

    <div class="brand">
      <span class="brand__dot"></span>
      <span class="brand__name">skyNOMAD.com</span>
    </div>

    <h1 class="headline">Gulfside Rotor<br>Flights</h1>

    <div class="site-link">
      <svg class="site-link__icon" viewBox="0 0 30 30" aria-hidden="true">
        <g fill="none" stroke="var(--text-white)" stroke-width="2">
          <circle cx="15" cy="15" r="12"/>
          <ellipse cx="15" cy="15" rx="5.5" ry="12"/>
          <line x1="3" y1="15" x2="27" y2="15"/>
          <path d="M5 8.5 H25 M5 21.5 H25"/>
        </g>
      </svg>
      <span class="site-link__url">skyNOMAD.com</span>
    </div>
  </section>
</body>
</html>
```